Flashy and colorful banner for an orange grower

Hi, I need a graphic for an advertising banner (80x200cm) to be placed next to the sales van. So far we have tried to highlight the naturalness of our products. With this banner we would like to highlight the ancient Sicilian tradition, with the typical decorations, I attach some photos as an example. We will sell our products far from Sicily, so I would like to exalt our origin.
We would like to dare with a colorful and amazing design, to capture the attention of passers-by.
It might be nice to insert or rework the decoration within our logo.
I would like to insert 4 of our offers inside the banner, only in the upper part, from the middle up.
The text is:
DAL CUORE DELLA SICILIA
ARANCIA TAROCCO
ALLA RINFUSA
5€ BORSA
DA SPREMERE
10€ CASSETTA
DA TAVOLA
15€ CASSETTA
SELEZIONE PREMIUM
20€ CASSETTA
Thanks for your time

```html
<!DOCTYPE html>
<html lang="it">
<head>
<meta charset="utf-8">
<title>Aurantia Sicilia – Banner Arancia Tarocco</title>
<link rel="stylesheet" href="https://fonts.googleapis.com/css2?family=Lato:wght@700;900&display=swap">
<style>
  :root {
    --cream: #f9df9a;
    --white: #ffffff;
    --green-dark: #11693a;
    --green: #2a8a3e;
    --green-deep: #146b35;
    --orange-light: #f6a024;
    --orange-red: #e05a26;
    --orange: #f08024;
    --orange-gold: #f0a83a;
    --page: #f2f2f2;
  }
  html, body {
    margin: 0;
    width: 1200px;
    height: 1200px;
    overflow: hidden;
    background: var(--page);
  }
  .stage {
    position: relative;
    width: 1200px;
    height: 1200px;
  }
  .banner {
    position: absolute;
    left: 380px;
    top: 50px;
    width: 440px;
    height: 1100px;
    box-shadow: 0 4px 14px rgba(0,0,0,0.12);
  }
  .banner text { font-family: 'Lato', sans-serif; }
  .headline { font-weight: 900; fill: var(--green-dark); }
  .variety { font-weight: 900; fill: var(--white); }
  .offer-label { font-weight: 700; fill: var(--white); font-size: 24px; }
  .offer-price { font-weight: 900; fill: var(--white); font-size: 42px; }
  .offer-unit { font-weight: 700; fill: var(--white); font-size: 13px; }
  .brand-name { font-weight: 900; fill: var(--green-dark); font-size: 32px; }
  .brand-tagline { font-weight: 700; fill: var(--orange-red); font-size: 10px; letter-spacing: 3px; }
  .website { font-weight: 900; fill: var(--white); font-size: 18px; letter-spacing: 2px; }
</style>
</head>
<body>
<div class="stage">
  <svg class="banner" viewBox="0 0 440 1100" width="440" height="1100" xmlns="http://www.w3.org/2000/svg">
    <defs>
      <linearGradient id="green-field" x1="0" y1="0" x2="1" y2="1">
        <stop offset="0" stop-color="var(--green)"/>
        <stop offset="0.5" stop-color="var(--green-deep)"/>
        <stop offset="1" stop-color="var(--green)"/>
      </linearGradient>
      <linearGradient id="illustration-fill" x1="0" y1="0" x2="0" y2="1">
        <stop offset="0" stop-color="#4fa447"/>
        <stop offset="0.35" stop-color="#f4a640"/>
        <stop offset="1" stop-color="#ee8a2a"/>
      </linearGradient>
    </defs>

    <rect class="banner-base" x="0" y="0" width="440" height="1100" fill="var(--cream)"/>
    <rect class="decor-frame" x="22" y="20" width="396" height="1060" fill="none" stroke="var(--green-dark)" stroke-width="12" role="img" aria-label="Cornice decorativa siciliana a triangoli verdi e arancioni"/>
    <rect class="inner-panel" x="28" y="26" width="384" height="1048" fill="var(--white)"/>

    <path class="swoosh-top" d="M0 270 L0 312 Q40 318 62 330 L62 292 Q30 278 0 270 Z" fill="var(--orange-red)"/>
    <path class="green-field" d="M0 315 Q35 320 62 335 L384 335 L384 290 Q410 278 440 268 L440 840 Q330 820 250 840 Q120 880 0 950 Z" fill="url(#green-field)"/>
    <path class="swoosh-bottom" d="M300 822 Q380 818 440 830 L440 870 Q380 852 310 860 Z" fill="var(--orange-red)"/>
    <path class="swoosh-left" d="M0 960 Q60 915 120 895 Q70 925 0 975 Z" fill="var(--orange-red)"/>

    <!-- headline -->
    <text class="headline" x="67" y="90" font-size="50" textLength="179" lengthAdjust="spacingAndGlyphs">DAL CU</text>
    <rect class="headline-illustration" x="249" y="52" width="34" height="38" rx="6" fill="var(--orange)" role="img" aria-label="Piccola arancia decorata con foglia al posto della O"/>
    <text class="headline" x="287" y="90" font-size="50" textLength="64" lengthAdjust="spacingAndGlyphs">RE</text>
    <text class="headline" x="47" y="140" font-size="50" textLength="339" lengthAdjust="spacingAndGlyphs">DELLA SICILIA</text>

    <rect class="variety-pill" x="55" y="150" width="327" height="37" rx="18.5" fill="var(--orange-red)"/>
    <text class="variety" x="218.5" y="178" font-size="27" text-anchor="middle" textLength="300" lengthAdjust="spacingAndGlyphs">ARANCIA TAROCCO</text>

    <!-- offers -->
    <g class="offers">
      <path d="M58 227 Q58 213 72 213 L370 213 Q384 213 384 227 L384 301 L58 301 Z" fill="var(--orange-light)"/>
      <rect x="58" y="301" width="326" height="88" fill="var(--orange-red)"/>
      <rect x="58" y="389" width="326" height="88" fill="var(--orange)"/>
      <path d="M58 477 L384 477 L384 551 Q384 565 370 565 L72 565 Q58 565 58 551 Z" fill="var(--orange-gold)"/>

      <text class="offer-label" x="83" y="248">ALLA</text>
      <text class="offer-label" x="83" y="281">RINFUSA</text>
      <text class="offer-price" x="320" y="263" text-anchor="middle">05€</text>
      <text class="offer-unit" x="320" y="286" text-anchor="middle">BORSA</text>

      <text class="offer-label" x="83" y="336">DA</text>
      <text class="offer-label" x="83" y="369">SPREMERE</text>
      <text class="offer-price" x="320" y="351" text-anchor="middle">10€</text>
      <text class="offer-unit" x="320" y="374" text-anchor="middle">CASSETTA</text>

      <text class="offer-label" x="83" y="424">DA</text>
      <text class="offer-label" x="83" y="457">TAVOLA</text>
      <text class="offer-price" x="320" y="439" text-anchor="middle">15€</text>
      <text class="offer-unit" x="320" y="462" text-anchor="middle">CASSETTA</text>

      <text class="offer-label" x="83" y="512">SELEZIONE</text>
      <text class="offer-label" x="83" y="545">PREMIUM</text>
      <text class="offer-price" x="320" y="527" text-anchor="middle">20€</text>
      <text class="offer-unit" x="320" y="550" text-anchor="middle">CASSETTA</text>
    </g>

    <!-- illustration area -->
    <rect class="orange-illustration" x="88" y="590" width="270" height="340" rx="24" fill="url(#illustration-fill)" role="img" aria-label="Illustrazione di mezza arancia con decorazioni tradizionali siciliane e foglie verdi"/>

    <!-- brand -->
    <text class="brand-name" x="220" y="980" text-anchor="middle">AURANTIA SICILIA</text>
    <text class="brand-tagline" x="220" y="1007" text-anchor="middle">NATURALMENTE SICILIANA</text>

    <path class="website-band" d="M82 1027 L358 1027 L378 1064 L62 1064 Z" fill="var(--green-dark)"/>
    <text class="website" x="220" y="1052" text-anchor="middle">AURANTIASICILIA.COM</text>
  </svg>
</div>
</body>
</html>
```